B2B Energy Broker Website

Our current website looks amateur, we need something far more professional looking and advanced. Current website is www.halvorn-utilitypartners.com

```html
<!DOCTYPE html>
<html lang="en">
<head>
<meta charset="utf-8">
<title>Halvorn Utility Partners – Home</title>
<link href="https://fonts.googleapis.com/css2?family=Josefin+Sans:wght@300;400;600;700&display=swap" rel="stylesheet">
<style>
:root{
  --navy:#232a5c;
  --navy-deep:#1c2350;
  --blue:#3a6aaa;
  --blue-soft:#5a82bb;
  --panel:#e9eef5;
  --ink:#2a2d3a;
  --muted:#555a66;
  --footer:#17191d;
  --grey-bar:#a9a9ab;
  --white:#ffffff;
}
*{box-sizing:border-box;margin:0;padding:0}
html,body{width:1200px;height:4169px;overflow:hidden;background:#fff}
body{font-family:"Josefin Sans",sans-serif;color:var(--ink)}
.canvas{position:relative;width:1200px;height:4169px;overflow:hidden}
.page{position:absolute;left:117px;top:89px;width:970px;height:3998px;background:var(--white);box-shadow:0 4px 24px rgba(0,0,0,.12)}
.abs{position:absolute}

/* header */
.brand{left:238px;top:108px;display:flex;align-items:center;gap:10px}
.brand-dot{width:56px;height:56px;border-radius:50%;background:#3f4045}
.brand-name{font-size:26px;letter-spacing:5px;color:#3f4045;line-height:1}
.brand-sub{font-size:15px;color:#3f4045;margin-top:4px}
.top-contact{top:110px;font-size:13px;color:var(--ink);display:flex;align-items:center;gap:7px}
.nav{top:146px;left:594px;display:flex;gap:32px;font-size:13px;font-weight:700;color:var(--navy)}
.nav .active{position:relative}
.nav .active::after{content:"";position:absolute;left:0;right:0;bottom:-14px;height:3px;background:var(--navy)}
.btn-contact{left:931px;top:139px;width:110px;height:30px;background:var(--navy);color:#fff;font-size:13px;font-weight:700;display:flex;align-items:center;justify-content:center}

/* hero */
.hero{left:117px;top:182px;width:970px;height:386px;background:linear-gradient(120deg,#2d3e6e 0%,#3e5586 45%,#5d78a8 100%)}
.hero-title{left:238px;top:272px;color:#fff;font-size:35px;line-height:44px;letter-spacing:.5px}
.hero-title b{font-weight:700}
.hero-sub{left:238px;top:368px;color:#fff;font-size:21px;font-weight:300}
.hero-globe{left:649px;top:216px;width:314px;height:314px;border-radius:50%;border:9px solid #c9cbd0;background:radial-gradient(circle at 55% 55%,#3a4a6b 0%,#1a2137 70%)}
.grey-bar{height:21px;border-radius:0 11px 11px 0;background:linear-gradient(90deg,#fff 0%,var(--grey-bar) 40%,#8e8e90 100%)}

/* buttons with circle arrow */
.btn-arrow{display:flex;align-items:center;justify-content:center;font-size:11px;font-weight:700;letter-spacing:.3px}
.btn-arrow .circ{position:absolute;right:-14px;top:50%;transform:translateY(-50%);width:28px;height:28px;border-radius:50%;background:var(--blue);display:flex;align-items:center;justify-content:center}
.btn-solid{background:var(--blue);color:#fff;border:2px solid #fff}
.btn-solid .circ{background:transparent;border:2px solid #fff}
.btn-line{background:#fff;color:var(--navy);border:2px solid var(--navy)}

/* welcome */
.kicker{font-size:19px;color:var(--ink)}
.section-title{font-size:28px;font-weight:700;color:var(--navy)}
.rule{height:2px;background:#a8b7d3}
.welcome-photo{left:240px;top:746px;width:198px;height:243px;background:linear-gradient(180deg,#cfe1f0 0%,#9fb8d0 55%,#6d86a8 100%)}
.half-disc{left:164px;top:792px;width:152px;height:152px;border-radius:50%;background:var(--blue)}
.welcome-copy{left:511px;top:747px;width:410px;font-size:12.5px;line-height:17px;color:var(--muted)}
.welcome-copy p{margin-bottom:10px;text-align:justify}
.welcome-copy b{color:var(--navy);font-weight:700}

/* services */
.services{left:161px;top:1064px;width:880px;height:777px;background:linear-gradient(160deg,#262d63 0%,#232a5c 60%,#2c3566 100%)}
.svc-head{left:161px;width:880px;text-align:center;color:#fff}
.svc{width:272px;text-align:center;color:#fff}
.svc-icon{width:88px;height:88px;border-radius:50%;background:#fff;margin:0 auto;display:flex;align-items:center;justify-content:center}
.svc-icon span{width:70px;height:70px;border-radius:50%;background:var(--blue);display:flex;align-items:center;justify-content:center}
.svc h3{font-size:16px;font-weight:700;margin-top:20px}
.svc p{font-size:12.5px;line-height:17px;margin-top:20px;color:#e6e8f2}

/* why */
.why-photo{left:657px;top:1800px;width:381px;height:523px;background:linear-gradient(180deg,#f1f2f4 0%,#cfd6e2 50%,#9eaac0 100%);border-radius:40% 40% 0 0}
.why-item{left:240px;width:360px;display:flex;gap:22px}
.tick{flex:none;width:58px;height:58px;border-radius:50%;background:#fff;box-shadow:0 2px 8px rgba(0,0,0,.18);display:flex;align-items:center;justify-content:center}
.tick span{width:46px;height:46px;border-radius:50%;background:var(--navy);display:flex;align-items:center;justify-content:center}
.why-item h4{font-size:16px;font-weight:700;color:var(--navy);margin-top:2px}
.why-item p{font-size:12.5px;line-height:17px;color:var(--muted);margin-top:8px;text-align:justify}

.helped{left:117px;width:970px;top:2410px;text-align:center;font-size:22px;line-height:30px;color:var(--navy)}
.partners{left:238px;top:2536px;width:682px;display:flex;justify-content:space-between;align-items:center;font-size:17px;font-weight:700;color:var(--navy)}

/* faq */
.cta{left:117px;top:3194px;width:970px;height:379px;background:linear-gradient(135deg,#4c74ad 0%,#5a80b8 50%,#4f76ae 100%)}
.faq{left:238px;top:2662px;width:727px;height:569px;background:var(--panel)}
.faq-title{left:238px;width:727px;top:2718px;text-align:center;font-size:22px;font-weight:700;color:var(--blue);letter-spacing:.5px}
.faq-item{left:285px;width:635px;height:75px;background:var(--navy);color:#fff;font-size:12.5px;font-weight:700;line-height:18px;padding:0 60px 0 26px;display:flex;align-items:center;letter-spacing:.2px}
.faq-item::after{content:"";position:absolute;right:26px;top:50%;margin-top:-3px;border:5px solid transparent;border-top:7px solid #fff;border-bottom:0}
.cta-title{left:117px;width:970px;top:3330px;text-align:center;color:#fff;font-size:27px;font-weight:700}

/* footer */
.footer{left:117px;top:3573px;width:970px;height:514px;background:var(--footer);color:#fff}
.f-mark{left:165px;top:3641px;width:146px;height:146px;border-radius:50%;background:#4a4b50}
.f-word{left:162px;top:3818px;font-size:32px;letter-spacing:9px}
.f-sub{left:162px;top:3868px;font-size:20px;font-weight:300}
.f-col h5{font-size:22px;font-weight:400}
.f-col .u{width:36px;height:2px;background:#fff;margin:12px 0 20px}
.f-col li{list-style:none;font-size:14px;margin-bottom:23px}
.f-contact{display:flex;gap:16px;align-items:flex-start;font-size:14px;line-height:21px;margin-bottom:12px}
.f-ico{flex:none;width:30px;height:30px;border-radius:50%;border:1.5px solid #fff;display:flex;align-items:center;justify-content:center}
.f-legal{left:117px;width:970px;text-align:center;font-size:13.5px;line-height:18px}
</style>
</head>
<body>
<div class="canvas">
  <div class="page"></div>

  <!-- Header -->
  <div class="abs brand">
    <div class="brand-dot"></div>
    <div>
      <div class="brand-name">HALVORN</div>
      <div class="brand-sub">utility partners</div>
    </div>
  </div>
  <div class="abs top-contact" style="left:678px">
    <svg width="13" height="13" viewBox="0 0 24 24"><path d="M6.6 10.8a15 15 0 0 0 6.6 6.6l2.2-2.2a1 1 0 0 1 1-.25 11 11 0 0 0 3.6.6 1 1 0 0 1 1 1V20a1 1 0 0 1-1 1A17 17 0 0 1 3 4a1 1 0 0 1 1-1h3.5a1 1 0 0 1 1 1 11 11 0 0 0 .6 3.6 1 1 0 0 1-.25 1z" fill="none" stroke="#2a2d3a" stroke-width="2"/></svg>
    0330 555 0147
  </div>
  <div class="abs top-contact" style="left:824px;font-size:12px">
    <svg width="14" height="14" viewBox="0 0 24 24"><circle cx="12" cy="12" r="10" fill="none" stroke="#2a2d3a" stroke-width="2"/><circle cx="12" cy="12" r="4" fill="none" stroke="#2a2d3a" stroke-width="2"/></svg>
    info@halvorn-utilitypartners.com
  </div>
  <nav class="abs nav">
    <span class="active">Home</span><span>About Us</span><span>Services</span><span>FAQs</span>
  </nav>
  <div class="abs btn-contact">Contact Us</div>

  <!-- Hero -->
  <div class="abs hero" role="img" aria-label="Night view of Earth from orbit with city lights"></div>
  <div class="abs hero-globe" role="img" aria-label="Circular photo of city lights at night"></div>
  <h1 class="abs hero-title" style="font-weight:400">TRANSPARENT<br><b>ENERGY SAVINGS</b></h1>
  <div class="abs hero-sub">Unbiased For your Business</div>
  <div class="abs btn-arrow btn-solid" style="left:238px;top:421px;width:151px;height:45px">TALK TO US
    <span class="circ"><svg width="14" height="14" viewBox="0 0 24 24"><path d="M5 12h13M13 6l6 6-6 6" fill="none" stroke="#fff" stroke-width="2.5"/></svg></span>
  </div>
  <div class="abs grey-bar" style="left:117px;top:558px;width:321px"></div>

  <!-- Welcome -->
  <div class="abs kicker" style="left:238px;top:620px">Welcome To</div>
  <h2 class="abs section-title" style="left:238px;top:648px">HALVORN UTILITY PARTNERS</h2>
  <div class="abs rule" style="left:238px;top:701px;width:107px"></div>
  <div class="abs half-disc"></div>
  <div class="abs welcome-photo" role="img" aria-label="Two engineers in hard hats walking beside solar panels and wind turbines"></div>
  <div class="abs welcome-copy">
    <p>Along with <b>providing competitive business energy procurement</b>, we run a <b>complete service solution for your ongoing energy requirements.</b></p>
    <p>We can take total management of your <b>bills, supplier relationship, renewals and more.</b></p>
    <p>If you are concerned about a more complex arrangement for your energy supply, then we will endeavour to take over the time spent on it and allow you as much or as little involvement as you desire.</p>
  </div>
  <div class="abs btn-arrow btn-line" style="left:511px;top:944px;width:130px;height:44px">LEARN MORE
    <span class="circ"><svg width="14" height="14" viewBox="0 0 24 24"><path d="M5 12h13M13 6l6 6-6 6" fill="none" stroke="#fff" stroke-width="2.5"/></svg></span>
  </div>

  <!-- Services -->
  <section class="abs services" role="img" aria-label="Dark navy panel over a faint city skyline"></section>
  <div class="abs svc-head" style="top:1106px;font-size:22px;font-weight:300">Our</div>
  <h2 class="abs svc-head" style="top:1136px;font-size:28px;font-weight:700">SERVICES</h2>
  <div class="abs rule" style="left:548px;top:1191px;width:108px;background:#4f5d92"></div>

  <div class="abs svc" style="left:284px;top:1250px">
    <div class="svc-icon"><span><svg width="34" height="34" viewBox="0 0 24 24"><rect x="5" y="6" width="14" height="15" rx="1" fill="none" stroke="#fff" stroke-width="1.6"/><path d="M8 6V3h5l2 3M9 11h6v6H9z" fill="none" stroke="#fff" stroke-width="1.6"/></svg></span></div>
    <h3>Commercial Gas</h3>
    <p>We offer an impartial review of your business gas requirements to ensure you are getting the best prices, service and management as a total package.</p>
  </div>
  <div class="abs svc" style="left:631px;top:1250px">
    <div class="svc-icon"><span><svg width="34" height="34" viewBox="0 0 24 24"><path d="M12 6a5 5 0 0 0-3 9v2h6v-2a5 5 0 0 0-3-9zM10 19h4M12 1v2M4 5l1.5 1.5M20 5l-1.5 1.5M2 12h2M20 12h2" fill="none" stroke="#fff" stroke-width="1.6"/></svg></span></div>
    <h3>Commercial Electricity</h3>
    <p>We offer an impartial review of your business electricity requirements to ensure you are getting the best prices, service and management as a total package.</p>
  </div>
  <div class="abs svc" style="left:284px;top:1546px">
    <div class="svc-icon"><span><svg width="34" height="34" viewBox="0 0 24 24"><path d="M5 19L15 9M14 5a4 4 0 0 0 5 5l-2-2-1-2zM19 19L9 9M5 5l3 1 1 3-3-1z" fill="none" stroke="#fff" stroke-width="1.8"/></svg></span></div>
    <h3>Utility Services</h3>
    <p>We can provide a wide range of business utility management services to ensure your time and money is better spent.</p>
  </div>
  <div class="abs svc" style="left:631px;top:1546px">
    <div class="svc-icon"><span><svg width="30" height="30" viewBox="0 0 24 24"><path d="M12 2s-7 8-7 13a7 7 0 0 0 14 0c0-5-7-13-7-13z" fill="#fff"/></svg></span></div>
    <h3>Commercial Water</h3>
    <p>The commercial water market has now been de-regulated. Speak to our team to find out how we can save you money on your water and waste bills.</p>
  </div>

  <!-- Why choose us -->
  <div class="abs grey-bar" style="left:238px;top:1830px;width:179px"></div>
  <div class="abs why-photo" role="img" aria-label="Smiling engineer in a white hard hat holding a tablet"></div>
  <h2 class="abs" style="left:238px;top:1908px;font-size:28px;color:var(--navy);font-weight:400">WHY <b>CHOOSE US</b></h2>

  <div class="abs why-item" style="top:1999px">
    <div class="tick"><span><svg width="22" height="22" viewBox="0 0 24 24"><path d="M5 12l5 5 9-10" fill="none" stroke="#fff" stroke-width="3"/></svg></span></div>
    <div><h4>Market Trend Analysis</h4><p>Our energy analysts monitor a live energy market curve to ensure you buy at the right time and save as much as possible.</p></div>
  </div>
  <div class="abs why-item" style="top:2123px">
    <div class="tick"><span><svg width="22" height="22" viewBox="0 0 24 24"><path d="M5 12l5 5 9-10" fill="none" stroke="#fff" stroke-width="3"/></svg></span></div>
    <div><h4>Direct Relationships</h4><p>We hold direct relationships with over 18 major suppliers, we use these relationships to ensure you get the most from your supplier.</p></div>
  </div>
  <div class="abs why-item" style="top:2248px">
    <div class="tick"><span><svg width="22" height="22" viewBox="0 0 24 24"><path d="M5 12l5 5 9-10" fill="none" stroke="#fff" stroke-width="3"/></svg></span></div>
    <div><h4>Industry Experience</h4><p>Our two founders hold over 30 years industry experience between them and our staff are what we believe to be the best in the industry.</p></div>
  </div>

  <p class="abs helped">We have helped businesses of all sizes<br>with our clean energy solutions, including:</p>
  <div class="abs partners">
    <span>Northmere</span><span>Velsta Energy</span><span>Brightwell</span><span>Solvane</span><span>Kestral</span><span>Oriel</span>
  </div>

  <!-- CTA band -->
  <section class="abs cta" role="img" aria-label="Blue-tinted street map background"></section>

  <!-- FAQ -->
  <div class="abs faq"></div>
  <h2 class="abs faq-title">FREQUENTLY ASKED QUESTIONS</h2>
  <div class="abs faq-item" style="top:2793px">WHY SHOULD MY BUSINESS USE HALVORN UTILITY PARTNERS?</div>
  <div class="abs faq-item" style="top:2895px">WHY SHOULD MY BUSINESS USE HALVORN UTILITY PARTNERS?</div>
  <div class="abs faq-item" style="top:2996px">ONCE I HAVE SIGNED A CONTRACT, IS THERE A COOLING OFF PERIOD IF I CHANGE MY MIND?</div>
  <div class="abs btn-arrow btn-line" style="left:530px;top:3127px;width:129px;height:44px">VIEW ALL
    <span class="circ"><svg width="14" height="14" viewBox="0 0 24 24"><path d="M5 12h13M13 6l6 6-6 6" fill="none" stroke="#fff" stroke-width="2.5"/></svg></span>
  </div>

  <h2 class="abs cta-title">Ready to have your energy needs taken care of?</h2>
  <div class="abs btn-arrow btn-line" style="left:530px;top:3411px;width:129px;height:44px;border-color:#fff">CONTACT US
    <span class="circ"><svg width="14" height="14" viewBox="0 0 24 24"><path d="M5 12h13M13 6l6 6-6 6" fill="none" stroke="#fff" stroke-width="2.5"/></svg></span>
  </div>

  <!-- Footer -->
  <footer class="abs footer"></footer>
  <div class="abs f-mark"></div>
  <div class="abs f-word" style="color:#fff">HALVORN</div>
  <div class="abs f-sub" style="color:#fff">utility partners</div>

  <div class="abs f-col" style="left:389px;top:3636px;color:#fff">
    <h5>Menu</h5><div class="u"></div>
    <ul><li>Home</li><li>About Us</li><li>Services</li><li style="font-size:13px">FAQs</li></ul>
  </div>
  <div class="abs f-col" style="left:538px;top:3636px;color:#fff">
    <h5>Quick Links</h5><div class="u"></div>
    <ul><li>Privacy Policy</li><li>Cookie Policy</li><li>Terms &amp; Conditions</li></ul>
  </div>
  <div class="abs f-col" style="left:761px;top:3636px;color:#fff">
    <h5>Contacts</h5><div class="u"></div>
    <div class="f-contact"><span class="f-ico"><svg width="14" height="14" viewBox="0 0 24 24"><path d="M12 22s7-7 7-12a7 7 0 0 0-14 0c0 5 7 12 7 12z" fill="none" stroke="#fff" stroke-width="2"/><circle cx="12" cy="10" r="2.5" fill="#fff"/></svg></span><span>Unit 4,<br>12 Marlow Street, Kettering,<br>NN9 4TR</span></div>
    <div class="f-contact"><span class="f-ico"><svg width="13" height="13" viewBox="0 0 24 24"><path d="M6.6 10.8a15 15 0 0 0 6.6 6.6l2.2-2.2a1 1 0 0 1 1-.25 11 11 0 0 0 3.6.6 1 1 0 0 1 1 1V20a1 1 0 0 1-1 1A17 17 0 0 1 3 4a1 1 0 0 1 1-1h3.5a1 1 0 0 1 1 1 11 11 0 0 0 .6 3.6 1 1 0 0 1-.25 1z" fill="none" stroke="#fff" stroke-width="2"/></svg></span><span style="line-height:30px">0330 555 0147</span></div>
    <div class="f-contact"><span class="f-ico"><svg width="14" height="14" viewBox="0 0 24 24"><rect x="4" y="7" width="16" height="12" rx="1" fill="none" stroke="#fff" stroke-width="2"/><path d="M7 7V3h10v4M8 11h8M8 15h8" stroke="#fff" stroke-width="1.6"/></svg></span><span style="line-height:30px">0330 555 0147</span></div>
    <div class="f-contact"><span class="f-ico"><svg width="14" height="14" viewBox="0 0 24 24"><circle cx="12" cy="12" r="9" fill="none" stroke="#fff" stroke-width="2"/><circle cx="12" cy="12" r="3.5" fill="none" stroke="#fff" stroke-width="2"/></svg></span><span style="line-height:30px">info@halvorn-utilitypartners.com</span></div>
  </div>

  <p class="abs f-legal" style="top:3968px;color:#fff">© Halvorn Utility Partners 2022</p>
  <p class="abs f-legal" style="top:4005px;color:#fff;padding:0 190px">All customer data will be retained securely in line with the data protection act. The data stored will only be used for the intended purposes of utility contracting and will be sent to the relevant supplier when necessary.</p>
</div>
</body>
</html>
```